Jewellery retailer needs a flyer design please

We need a flyer to represent our business.

Our company provides The lowest priced diamonds in Australia.
We are wholesales who sell direct to the public
We GENUINELY are 50-70% cheaper than other retail stores.

We guarantee the lowest prices, even in the unlikely event a customer finds a cheaper price than ours, we will beat it too.

Well tell our customers if youre not buying from us then you're paying too much.

Please include website www.tarvenhollow.com.au
and facebook page www.pagenook.com/quillbramsey.

We have location in Harbourlea Parramatta, and Harbourlea Liverpool, NSW.

Im sorry, this is the first time ive done this, so i hope ive given the information you need.

Target Market(s)

People wanting to buy engagement rings are our biggest customers.

Industry/Entity Type

Retail

Colors
276db0
3276b5
86acd3
cedeed

Requirements
Must have
• Simple, to the point! We need people to know that we have the lowest prices without compromising on quality
Nice to have
• I am very very open to anything. I do not have any particular expectations

```html
<!DOCTYPE html>
<html lang="en">
<head>
<meta charset="utf-8">
<title>Tarven Hollow Flyer</title>
<link rel="stylesheet" href="https://fonts.googleapis.com/css2?family=Jost:wght@400;500&display=swap">
<style>
  :root {
    --stage: #2b2b2b;
    --flyer-top: #6c6c6c;
    --flyer-bottom: #3f3f3f;
    --band: #7e7e7e;
    --ornament: #6e6e6e;
    --logo-bg: #ffffff;
    --logo-border: #a9a9a9;
    --logo-ink: #3d4f75;
    --text: #ffffff;
    --tab: #3a3a3a;
    --tab-text: #d8d8d8;
    --info-band: rgba(170, 170, 170, 0.6);
    --info-text: #2a2a2a;
    --photo-backdrop: #5c5c5e;
    --photo-leather: #1e1e20;
    --photo-silver: #e4e4ea;
    --photo-gem: #9a2fd6;
    --photo-gem-deep: #5a1a8c;
  }
  * { margin: 0; padding: 0; box-sizing: border-box; }
  html, body { width: 1200px; height: 1172px; overflow: hidden; background: var(--stage); }
  body { font-family: "Jost", "Futura", sans-serif; }

  .flyer {
    position: absolute; left: 205px; top: 26px; width: 790px; height: 1120px;
    background: linear-gradient(180deg, var(--flyer-top) 0%, #5a5a5a 40%, var(--flyer-bottom) 100%);
    overflow: hidden;
  }
  .header-band { position: absolute; left: 0; top: 78px; width: 100%; height: 72px; background: var(--band); }
  .band-ornament { position: absolute; top: 96px; width: 120px; height: 36px; background: var(--ornament); opacity: 0.6; border-radius: 18px; }
  .band-ornament.left { left: 45px; }
  .band-ornament.right { right: 45px; }

  .logo-box {
    position: absolute; left: 240px; top: 31px; width: 320px; height: 169px;
    background: var(--logo-bg); border: 6px solid var(--logo-border);
    display: flex; align-items: center; justify-content: center; gap: 12px;
  }
  .logo-mark { width: 14px; height: 14px; border-radius: 50%; background: var(--logo-ink); }
  .logo-name { font-weight: 400; font-size: 40px; color: var(--logo-ink); letter-spacing: 1px; }

  .guarantee { position: absolute; top: 214px; width: 100%; text-align: center; color: var(--text); font-size: 22px; line-height: 31px; }
  .headline { position: absolute; color: var(--text); font-size: 30px; font-weight: 400; line-height: 1; white-space: nowrap; }
  .headline.one { left: 77px; top: 312px; }
  .headline.two { left: 121px; top: 354px; }
  .claim { position: absolute; width: 100%; text-align: center; color: var(--text); font-size: 23px; }
  .claim.one { top: 414px; }
  .claim.two { top: 455px; }

  .product-photo {
    position: absolute; left: 0; top: 500px; width: 100%; height: 620px;
    background:
      radial-gradient(ellipse 17% 19% at 47% 31%, var(--photo-gem) 0%, var(--photo-gem-deep) 70%, rgba(90,26,140,0) 100%),
      radial-gradient(ellipse 24% 27% at 47% 31%, var(--photo-silver) 0%, rgba(228,228,234,0.75) 60%, rgba(228,228,234,0) 100%),
      radial-gradient(ellipse 48% 10% at 47% 36%, rgba(210,210,216,0.7) 0%, rgba(210,210,216,0) 100%),
      linear-gradient(180deg, rgba(92,92,94,0) 0%, var(--photo-backdrop) 18%, #48484a 45%, var(--photo-leather) 62%, #151517 100%);
  }

  .locations-tab {
    position: absolute; left: 0; top: 982px; width: 205px; height: 34px;
    background: var(--tab); color: var(--tab-text); font-size: 19px; font-weight: 500;
    padding-left: 36px; line-height: 34px;
  }
  .info-band { position: absolute; left: 0; top: 1016px; width: 100%; height: 104px; background: var(--info-band); }
  .location-list { position: absolute; left: 36px; top: 1020px; list-style: none; }
  .location-list li { color: var(--info-text); font-size: 20px; line-height: 34px; padding-left: 24px; position: relative; }
  .location-list li::before { content: ""; position: absolute; left: 0; top: 14px; width: 7px; height: 7px; border-radius: 50%; background: var(--info-text); }
  .web-links { position: absolute; left: 388px; top: 1020px; }
  .web-links p { color: var(--info-text); font-size: 20px; line-height: 34px; }
</style>
</head>
<body>
  <main class="flyer">
    <div class="header-band"></div>
    <div class="band-ornament left" role="img" aria-label="Decorative scroll flourish"></div>
    <div class="band-ornament right" role="img" aria-label="Decorative scroll flourish"></div>

    <div class="logo-box">
      <span class="logo-mark"></span>
      <span class="logo-name">Tarven Hollow</span>
    </div>

    <p class="guarantee">We guarantee the lowest prices, even in the unlikely event a<br>customer finds a cheaper price than ours, we will beat it too.</p>
    <h1 class="headline one">Lowest Priced Diamonds in Australia</h1>
    <h2 class="headline two">Wholesalers who sell direct to the public</h2>
    <p class="claim one">We GENUINELY are 50-70% cheaper than other retail stores.</p>
    <p class="claim two">If you're not buying from us then you're paying too much.</p>

    <div class="product-photo" role="img" aria-label="Photo of a cushion-cut purple gemstone ring with a diamond halo resting on dark leather"></div>

    <div class="locations-tab">Our Locations</div>
    <div class="info-band"></div>
    <ul class="location-list">
      <li>Harbourlea Parramatta, NSW</li>
      <li>Harbourlea Liverpool, NSW</li>
    </ul>
    <div class="web-links">
      <p>www.tarvenhollow.com.au</p>
      <p>www.pagenook.com/quillbramsey</p>
    </div>
  </main>
</body>
</html>
```